I need a label design/logo for a Shea Body Butter that I making. The body butter is made using Unrefined Shea Butter from Uganda. I have different mixes for the body butter depending on the Essential Oil used, for example - sweet orange, lavender, rosemary. The species of Shea tree in Uganda (Vitellaria Nilotica) is different from the one in West Africa (Vitellaria Paradoxa). As such, I would like the logo/label to have some reference to the Shea nut tree as well as the River Nile. Colours should be "fresh and earthy". I will be using round containers and I would like to be able to place the logo/label on round templates that I can stick on the containers. The name of the brand is "Teka Rumi" Shea Body Butter.

```html
<!DOCTYPE html>
<html lang="en">
<head>
<meta charset="utf-8">
<title>Teka Rumi Nile Body Cream Label</title>
<link rel="stylesheet" href="https://fonts.googleapis.com/css2?family=Work+Sans:wght@300;400;600;700&display=swap">
<style>
  :root {
    --ink: #4a4a4a;
    --accent: #f05a28;
    --paper: #ffffff;
  }
  html, body {
    margin: 0;
    padding: 0;
    width: 1200px;
    height: 1000px;
    overflow: hidden;
    background: var(--paper);
  }
  .label {
    position: relative;
    width: 1200px;
    height: 1000px;
    font-family: "Work Sans", Arial, sans-serif;
    color: var(--ink);
  }
  .label__arc {
    position: absolute;
    left: 0;
    top: 0;
  }
  .label__arc-text {
    font-family: "Work Sans", Arial, sans-serif;
    font-size: 20px;
    font-weight: 400;
    letter-spacing: 3px;
    fill: var(--ink);
  }
  .brand-mark {
    position: absolute;
    left: 440px;
    top: 440px;
    width: 110px;
    height: 110px;
    border-radius: 50%;
    background: var(--accent);
  }
  .brand-name {
    position: absolute;
    left: 400px;
    top: 568px;
    width: 190px;
    text-align: center;
    font-size: 28px;
    font-weight: 400;
    color: var(--accent);
    margin: 0;
    white-space: nowrap;
  }
  .label__rule {
    position: absolute;
    left: 591px;
    top: 422px;
    width: 2px;
    height: 270px;
    background: var(--ink);
  }
  .product-name {
    position: absolute;
    left: 604px;
    top: 430px;
    margin: 0;
    font-size: 62px;
    font-weight: 300;
    line-height: 60px;
    color: var(--ink);
    white-space: nowrap;
  }
  .product-name span { display: block; }
  .net-weight {
    position: absolute;
    left: 480px;
    top: 660px;
    width: 88px;
    text-align: right;
    font-size: 20px;
    font-weight: 400;
    margin: 0;
  }
  .ingredients {
    position: absolute;
    left: 608px;
    top: 636px;
    margin: 0;
  }
  .ingredients__title {
    font-size: 13px;
    font-weight: 700;
    letter-spacing: 1.5px;
    margin: 0 0 4px;
  }
  .ingredients__list {
    font-size: 12.5px;
    font-weight: 600;
    line-height: 16px;
    margin: 0;
  }
</style>
</head>
<body>
  <main class="label">
    <svg class="label__arc" width="1200" height="1000" viewBox="0 0 1200 1000" aria-hidden="true">
      <defs>
        <path id="origin-arc" d="M 358 565 A 248 248 0 0 1 854 565" fill="none"/>
      </defs>
      <text class="label__arc-text">
        <textPath href="#origin-arc" startOffset="1%">MADE FROM UNREFINED SHEA BUTTER FROM UGANDA</textPath>
      </text>
      <circle cx="375" cy="597" r="6" fill="var(--ink)"/>
      <circle cx="841" cy="478" r="6" fill="var(--ink)"/>
    </svg>

    <div class="brand-mark"></div>
    <p class="brand-name">Teka Rumi</p>

    <div class="label__rule"></div>

    <h1 class="product-name">
      <span>nile</span>
      <span>body</span>
      <span>cream</span>
    </h1>

    <p class="net-weight">50 g</p>

    <div class="ingredients">
      <p class="ingredients__title">INGREDIENTS:</p>
      <p class="ingredients__list">SHEA BUTTER, COCONUT OIL<br>&amp; ESSENTIAL OIL</p>
    </div>
  </main>
</body>
</html>
```